Business Card Design Project

1. Show the company logo.
2. Only company email ID and website address to be shown (office@tikhayavolna.fm , www.tikhayavolna.fm).
3. Logo to be provided by us, 2 designs just in case. The logo is made with ' Tikhaya Volna' text, need to be edited so that it shows 'Yasnaya Afisha' instead .
4. Single sided business card, portrait or landscape is not a problem; back side to be filled with colors or a design that matches the logo the best.
5. Logo is to be embossed.
6. We're looking at an English and Russian version.
7. any other better idea is always welcomed.

```html
<!DOCTYPE html>
<html lang="en">
<head>
<meta charset="utf-8">
<title>Yasnaya Afisha — Business Card</title>
<link rel="stylesheet" href="https://fonts.googleapis.com/css2?family=Questrial&display=swap">
<style>
  :root {
    --stage: #d9d9d9;
    --card-blue-deep: #1b3270;
    --card-blue: #27499a;
    --ring-blue: #203d82;
    --badge-blue: #1c3a7c;
    --badge-blue-light: #2c5099;
    --accent-gold: #f2b51c;
    --back-navy: #141f50;
    --back-navy-light: #1d2e68;
    --ink-light: #ffffff;
  }
  * { box-sizing: border-box; margin: 0; padding: 0; }
  html, body { width: 1200px; height: 900px; overflow: hidden; }
  body {
    background: var(--stage);
    font-family: "Questrial", sans-serif;
    position: relative;
  }
  .card {
    position: absolute;
    width: 700px;
    height: 400px;
    overflow: hidden;
    box-shadow: 0 6px 18px rgba(0,0,0,0.25);
  }
  .card--front {
    left: 60px;
    top: 50px;
    background: linear-gradient(200deg, var(--card-blue) 0%, var(--card-blue-deep) 100%);
  }
  .card--back {
    left: 440px;
    top: 470px;
  }
  .front-ring {
    position: absolute;
    left: -20px;
    top: 20px;
    width: 400px;
    height: 400px;
    border-radius: 50%;
    background: var(--ring-blue);
  }
  .logo-badge {
    position: absolute;
    left: 50px;
    top: 90px;
    width: 280px;
    height: 280px;
    border-radius: 50%;
    background: radial-gradient(circle at 50% 25%, var(--badge-blue-light) 0%, var(--badge-blue) 70%);
    box-shadow: inset 0 4px 10px rgba(255,255,255,0.08), 0 4px 12px rgba(0,0,0,0.25);
    display: flex;
    align-items: center;
    justify-content: center;
    gap: 14px;
    padding: 0 20px;
  }
  .logo-dot {
    width: 78px;
    height: 78px;
    border-radius: 50%;
    background: var(--accent-gold);
    flex: none;
  }
  .logo-name {
    color: var(--ink-light);
    font-size: 22px;
    line-height: 1.15;
    width: 120px;
  }
  .contact-list {
    position: absolute;
    left: 385px;
    top: 125px;
    list-style: none;
  }
  .contact-item {
    display: flex;
    align-items: center;
    gap: 12px;
    color: var(--ink-light);
    font-size: 24px;
    letter-spacing: 0.3px;
    margin-bottom: 14px;
  }
  .contact-icon { width: 22px; height: 22px; flex: none; }
  .back-pattern {
    width: 100%;
    height: 100%;
    background:
      radial-gradient(circle at 30% 30%, rgba(255,255,255,0.05) 0%, rgba(255,255,255,0) 60%),
      linear-gradient(200deg, var(--back-navy-light) 0%, var(--back-navy) 100%);
  }
</style>
</head>
<body>

  <section class="card card--front" aria-label="Business card front">
    <div class="front-ring"></div>
    <div class="logo-badge">
      <span class="logo-dot" aria-hidden="true"></span>
      <span class="logo-name">Yasnaya Afisha</span>
    </div>
    <ul class="contact-list">
      <li class="contact-item">
        <svg class="contact-icon" viewBox="0 0 20 20" aria-hidden="true">
          <rect x="1" y="4" width="18" height="12" fill="#fff"/>
          <path d="M1 4 L10 11 L19 4" fill="none" stroke="#27499a" stroke-width="1.4"/>
        </svg>
        office@tikhayavolna.fm
      </li>
      <li class="contact-item">
        <svg class="contact-icon" viewBox="0 0 20 20" aria-hidden="true" fill="none" stroke="#fff" stroke-width="1.4">
          <circle cx="10" cy="10" r="8.5"/>
          <ellipse cx="10" cy="10" rx="3.8" ry="8.5"/>
          <line x1="1.5" y1="10" x2="18.5" y2="10"/>
          <line x1="3" y1="5.5" x2="17" y2="5.5"/>
          <line x1="3" y1="14.5" x2="17" y2="14.5"/>
        </svg>
        www.tikhayavolna.fm
      </li>
    </ul>
  </section>

  <section class="card card--back" aria-label="Business card back">
    <div class="back-pattern" role="img" aria-label="Area for a repeating tone-on-tone brand monogram pattern in dark navy"></div>
  </section>

</body>
</html>
```